homepage design for online & live financial management course

homepage logo & required elements can be seen here -
http://kvt-portland.net/Index_new2011

we need a nice design to make it sing, and convert visitors to buyers

we like "Discover Hidden Profits in Your Business — Today!" but don't know how to incorporate it into the design

nice job! thanks for these submissions! keep it up -margaret @kvt/ledger summit (love the more elegant, simple lines of some of these!)

Industry/Entity Type

Financial

Requirements
Must have
• We need to have on the homepage -

- our logo (can not change) "Ledger Summit"
- our tag line (can not change) "Measure. Manage. Succeed."
- our 2-minute introductory video
- 2 options/buttons for visitor's next step: choose Online -or- Live

seen here -

```html
<!DOCTYPE html>
<html lang="en">
<head>
<meta charset="utf-8">
<title>Ledger Summit — Measure. Manage. Succeed.</title>
<link href="https://fonts.googleapis.com/css2?family=Open+Sans:wght@400;600&display=swap" rel="stylesheet">
<style>
  :root {
    --header-light: #ffffff;
    --header-grey: #d9d9d9;
    --brand-green: #0b5a3a;
    --teal: #1ca47f;
    --teal-deep: #1b977a;
    --band-dark: #1b3b33;
    --footer-teal: #22987a;
    --button-top: #fbfbfb;
    --button-bottom: #c4c4c4;
    --button-text: #2b2b2b;
    --button-sub: #114a2e;
    --player-frame: #161616;
    --player-bar: #262626;
    --white: #ffffff;
  }
  * { box-sizing: border-box; margin: 0; padding: 0; }
  html, body { width: 1200px; height: 1006px; overflow: hidden; }
  body { font-family: "Open Sans", Arial, sans-serif; position: relative; background: var(--teal); }

  .site-header {
    position: absolute; left: 0; top: 0; width: 1200px; height: 366px;
    background: radial-gradient(ellipse at 45% 40%, var(--header-light) 0%, #f2f2f2 45%, var(--header-grey) 100%);
  }
  .brand { position: absolute; left: 66px; top: 70px; display: flex; align-items: center; gap: 18px; }
  .brand-name {
    color: var(--brand-green); font-weight: 600; font-size: 60px; line-height: 66px;
    text-transform: uppercase; letter-spacing: 1px;
  }
  .brand-mark { width: 108px; height: 108px; border-radius: 50%; background: var(--brand-green); flex: none; }
  .tagline {
    position: absolute; left: 60px; top: 236px; width: 391px; height: 38px;
    border-radius: 6px; border: 1px solid #9a9a9a;
    background: linear-gradient(var(--button-top), var(--button-bottom));
    color: var(--button-text); font-size: 26px; line-height: 36px; text-align: center;
  }
  .hero-art {
    position: absolute; left: 744px; top: 18px; width: 408px; height: 342px;
    background: linear-gradient(120deg, #f1f1f1 0%, #f7b27a 35%, #c8e85a 60%, #6fd0e8 85%, #f1f1f1 100%);
    opacity: 0.75; border-radius: 8px;
  }

  .showcase {
    position: absolute; left: 0; top: 366px; width: 1200px; height: 458px;
    background: linear-gradient(var(--teal), var(--teal-deep));
  }
  .section-label { position: absolute; left: 54px; top: 24px; color: var(--white); font-size: 24px; }
  .video-player {
    position: absolute; left: 52px; top: 68px; width: 628px; height: 340px;
    background: var(--player-frame); border-radius: 7px;
  }
  .video-poster {
    position: absolute; left: 6px; top: 6px; width: 616px; height: 291px;
    background: linear-gradient(160deg, #ffffff 0%, #f4f9e6 45%, #b9dc4f 80%, #8fc23a 100%);
  }
  .video-controls { position: absolute; left: 6px; top: 297px; width: 616px; height: 37px; }
  .video-controls svg { display: block; }
  .video-time { position: absolute; left: 110px; top: 10px; font-size: 12px; color: var(--white); }
  .video-time span { color: #9a9a9a; }
  .video-quality { position: absolute; left: 516px; top: 10px; font-size: 12px; color: #bdbdbd; }

  .path-button {
    position: absolute; left: 756px; width: 378px; height: 119px;
    border-radius: 6px; border: 1px solid #8f8f8f;
    background: linear-gradient(var(--button-top), #e4e4e4 50%, var(--button-bottom));
    text-align: center; box-shadow: 0 2px 3px rgba(0,0,0,0.25);
  }
  .path-button.online { top: 83px; }
  .path-button.live { top: 242px; }
  .path-title { display: block; margin-top: 20px; font-size: 34px; color: var(--button-text); }
  .path-note { display: block; margin-top: 8px; font-size: 17px; color: var(--button-sub); }

  .promise-band {
    position: absolute; left: 0; top: 824px; width: 1200px; height: 113px;
    background: var(--band-dark); color: var(--white);
    font-size: 48px; line-height: 113px; text-align: center;
  }

  .site-footer {
    position: absolute; left: 0; top: 937px; width: 1200px; height: 69px; background: var(--footer-teal);
  }
  .copyright { position: absolute; left: 60px; top: 24px; font-size: 14px; color: var(--white); }
  .social-links { position: absolute; left: 1012px; top: 20px; display: flex; gap: 6px; }
  .social-links span { width: 29px; height: 29px; border-radius: 3px; display: block; }
  .social-links .s1 { background: #3b5b98; }
  .social-links .s2 { background: #5cc3e8; }
  .social-links .s3 { background: #1f6e9c; }
  .social-links .s4 { background: #e8701f; }
</style>
</head>
<body>
  <header class="site-header">
    <div class="brand">
      <div class="brand-name">Ledger<br>Summit</div>
      <div class="brand-mark"></div>
    </div>
    <div class="tagline">Measure. Manage. Succeed.</div>
    <div class="hero-art" role="img" aria-label="3D bar chart rising to a figure presenting success"></div>
  </header>

  <main class="showcase">
    <div class="section-label">VIDEO</div>
    <div class="video-player">
      <div class="video-poster" role="img" aria-label="Introductory video poster: green profit lettering under a rising arrow"></div>
      <div class="video-controls">
        <svg width="616" height="37" viewBox="0 0 616 37">
          <rect x="0" y="0" width="616" height="37" fill="#262626"/>
          <rect x="0" y="0" width="616" height="5" fill="#3a3a3a"/>
          <rect x="32" y="0" width="4" height="5" fill="#e0b020"/>
          <circle cx="9" cy="3" r="5" fill="#cfcfcf"/>
          <rect x="26" y="18" width="3" height="12" fill="#bbb"/>
          <rect x="33" y="18" width="3" height="12" fill="#bbb"/>
          <line x1="56" y1="9" x2="56" y2="37" stroke="#111"/>
          <path d="M70 21h5l6-5v16l-6-5h-5z" fill="#bbb"/>
          <path d="M85 19q4 5 0 10M89 17q6 7 0 14" stroke="#bbb" fill="none" stroke-width="1.5"/>
          <line x1="102" y1="9" x2="102" y2="37" stroke="#111"/>
          <line x1="558" y1="9" x2="558" y2="37" stroke="#111"/>
          <path d="M570 28v-8h12l-3-3M582 20l-3 3" stroke="#bbb" fill="none" stroke-width="1.5"/>
          <line x1="588" y1="9" x2="588" y2="37" stroke="#111"/>
          <path d="M596 18h4M596 18v4M610 18h-4M610 18v4M596 32h4M596 32v-4M610 32h-4M610 32v-4" stroke="#bbb" stroke-width="1.5"/>
        </svg>
        <div class="video-time">0:00 <span>/ 5:02</span></div>
        <div class="video-quality">360p</div>
      </div>
    </div>

    <a class="path-button online">
      <span class="path-title">Ledger Summit Online</span>
      <span class="path-note">Instantly learn how to unlock hidden profits</span>
    </a>
    <a class="path-button live">
      <span class="path-title">Ledger Summit Live</span>
      <span class="path-note">Learn about in-person events</span>
    </a>
  </main>

  <div class="promise-band">Discover Hidden Profits in Your Business — Today!</div>

  <footer class="site-footer">
    <div class="copyright">Copyright @ 1011. LedgerSummit.com All Rights Reserved</div>
    <div class="social-links">
      <span class="s1"></span><span class="s2"></span><span class="s3"></span><span class="s4"></span>
    </div>
  </footer>
</body>
</html>
```